RVT Business Card Design

We are an independent auto dealer who specializes in commercial & fleet vehicles, we are family owned and operated and have been in business since 2001. We stock late model, low mileage, white trucks & vans. We mostly deal with companies in the construction and service industries. We are just looking to try to freshen up our old business card, we do not want to change the logo at this point, because it is well know within the southwest region & construction community. I have attached our logo and a PDF of our current business card for reference.
Updates
If the address is stacked there is no comma (,) after NE. Everyone keeps putting it in with this format and it is not correct.
482 Montrose Ave NE
Albuquerque, NM 87193
If the address is all on one line, then there will be a comma (,) after NE
482 Montrose Ave NE, Albuquerque, NM 87193
Please make changes accordingly, thank you for your attention in this matter.
Industry/Entity Type
Construction
Contact Information for Business Card
482 Montrose Ave NE, Albuquerque, NM 87193, Dorian Wexhall, Vice President, dorian@rvtfleetmotors.com, www.RVTfleetmotors.com, ph 505-271-6048, fax 505-617-2094, cell 505-438-7720

```html
<!DOCTYPE html>
<html lang="en">
<head>
<meta charset="utf-8">
<title>RVT Auto Sales – Business Card</title>
<link href="https://fonts.googleapis.com/css2?family=Cinzel:wght@400;700&family=Marcellus&display=swap" rel="stylesheet">
<style>
  :root {
    --stage: #d9d4cc;
    --card-black: #0d0d0e;
    --card-black-soft: #1f1f21;
    --brand-red: #d3121b;
    --brand-red-dark: #8f0a10;
    --ink-white: #f2f2f2;
    --ink-grey: #bdbdbd;
    --rule: #5a5a5a;
  }
  * { box-sizing: border-box; margin: 0; padding: 0; }
  html, body { width: 1200px; height: 600px; overflow: hidden; }
  body {
    background: var(--stage);
    display: flex;
    align-items: center;
    justify-content: center;
    gap: 60px;
    font-family: "Marcellus", Georgia, serif;
  }
  .card {
    position: relative;
    width: 510px;
    height: 291px;
    background: linear-gradient(160deg, var(--card-black-soft) 0%, var(--card-black) 55%);
    box-shadow: 0 10px 24px rgba(0,0,0,.35);
    overflow: hidden;
    color: var(--ink-white);
  }

  /* ---------- front: contact side ---------- */
  .card-front .red-band {
    position: absolute; left: 0; right: 0; bottom: 0;
    height: 16px;
    background: linear-gradient(180deg, var(--brand-red) 0%, var(--brand-red-dark) 100%);
  }
  .brand-block { position: absolute; left: 30px; top: 24px; }
  .tagline {
    font-size: 9px; letter-spacing: .4px; color: var(--ink-grey);
    margin-bottom: 6px; margin-left: 2px;
  }
  .brand-name {
    font-family: "Cinzel", Georgia, serif;
    font-weight: 700; color: var(--ink-white);
    font-size: 30px; letter-spacing: 1px; line-height: 1;
    display: flex; align-items: center; gap: 8px;
  }
  .brand-mark { width: 10px; height: 10px; background: var(--brand-red); }
  .person { position: absolute; right: 30px; top: 30px; text-align: right; }
  .person-name {
    font-family: "Cinzel", Georgia, serif; font-weight: 700;
    color: var(--brand-red); font-size: 17px; letter-spacing: .5px;
  }
  .person-title {
    font-size: 11px; letter-spacing: 1.2px; text-transform: uppercase;
    color: var(--ink-white); margin-top: 3px;
  }
  .address {
    position: absolute; left: 30px; top: 112px;
    font-size: 12px; letter-spacing: .8px; text-transform: uppercase; color: var(--ink-white);
  }
  .divider {
    position: absolute; left: 30px; right: 30px; top: 138px;
    height: 1px; background: var(--rule);
  }
  .contact-list {
    position: absolute; left: 30px; top: 152px;
    list-style: none; font-size: 12px; line-height: 20px; letter-spacing: .6px;
  }
  .contact-list li { display: flex; align-items: center; gap: 10px; }
  .contact-list svg { width: 12px; height: 12px; flex: none; }
  .contact-list .web { color: var(--brand-red); }

  /* ---------- back: logo side ---------- */
  .card-back {
    display: flex; flex-direction: column; align-items: center; justify-content: center;
  }
  .card-back .tagline { font-size: 11px; margin-bottom: 10px; }
  .card-back .brand-name { font-size: 48px; gap: 12px; }
  .card-back .brand-mark { width: 14px; height: 14px; }
</style>
</head>
<body>

<section class="card card-front" aria-label="Business card, contact side">
  <div class="brand-block">
    <p class="tagline">Specializing in Commercial &amp; Fleet Vehicles</p>
    <p class="brand-name"><span class="brand-mark"></span>RVT Auto Sales</p>
  </div>

  <div class="person">
    <p class="person-name">Dorian Wexhall</p>
    <p class="person-title">Vice President</p>
  </div>

  <p class="address">482 Montrose Ave NE, Albuquerque, NM 87193</p>
  <div class="divider"></div>

  <ul class="contact-list">
    <li>
      <svg viewBox="0 0 12 12" aria-label="phone"><path fill="#f2f2f2" d="M2.5 1h2l1 2.5-1.3 1a6 6 0 0 0 3.3 3.3l1-1.3 2.5 1v2c0 .6-.4 1-1 1A9 9 0 0 1 1.5 2c0-.6.4-1 1-1z"/></svg>
      505-271-6048
    </li>
    <li>
      <svg viewBox="0 0 12 12" aria-label="fax"><rect x="3" y="1" width="6" height="3" fill="#f2f2f2"/><rect x="1" y="4.5" width="10" height="4.5" rx="1" fill="#f2f2f2"/><rect x="3" y="8" width="6" height="3" fill="#f2f2f2" stroke="#0d0d0e" stroke-width=".8"/></svg>
      505-617-2094
    </li>
    <li>
      <svg viewBox="0 0 12 12" aria-label="cell"><rect x="3" y=".5" width="6" height="11" rx="1" fill="#f2f2f2"/><rect x="4" y="2" width="4" height="6.5" fill="#0d0d0e"/></svg>
      505-438-7720
    </li>
    <li>
      <svg viewBox="0 0 12 12" aria-label="email"><rect x=".5" y="2.5" width="11" height="7" fill="#f2f2f2"/><path d="M.5 2.5 6 7l5.5-4.5" fill="none" stroke="#0d0d0e" stroke-width=".9"/></svg>
      dorian@rvtfleetmotors.com
    </li>
    <li class="web">
      <svg viewBox="0 0 12 12" aria-label="web"><circle cx="6" cy="6" r="5" fill="none" stroke="#d3121b" stroke-width="1.1"/><path d="M1 6h10M6 1c-2.5 3-2.5 7 0 10M6 1c2.5 3 2.5 7 0 10" fill="none" stroke="#d3121b" stroke-width=".9"/></svg>
      www.RVTfleetmotors.com
    </li>
  </ul>

  <div class="red-band"></div>
</section>

<section class="card card-back" aria-label="Business card, logo side">
  <p class="tagline">Specializing in Commercial &amp; Fleet Vehicles</p>
  <p class="brand-name"><span class="brand-mark"></span>RVT Auto Sales</p>
</section>

</body>
</html>
```